Online Consultancy Needs a New Logo & Business Card Design

Based on the new logo we just received from another contest here on Drawnest,

You'll find a few different versions of our logo as well as examples of business card designs we like in this folder:
==> https://files.velmorashare.net/view?id=7Kp2QwTx9LmRvZ4nHs8YbC1uF3aE&mode=open

We are considering two options:
- clean, black design
- clean, white/blue design

We're willing to consider both options.

We're considering adding some special effects to the cards when printing - emboss, rounded corners, etc.

However, please deliver a design WITHOUT round corners.

Target Market(s)

Successful business people, serious and older audience.

Industry/Entity Type

Business

Contact Information for Business Card

For the business card, I would like a minimalistic card with the logo on one side (perhaps in the middle) and the contact information on the other.

For the contact information please use:
Name: Peter Lang
Position: Founder
Email: peter.lang@morvel.com
Phone Number: +381 64 70 81 925
Website URL: www.morvel.com

Font styles to use
Serif
Sans Serif

Requirements
Must have
• Must fit in perfectly with our current website design.

```html
<!DOCTYPE html>
<html lang="en">
<head>
<meta charset="utf-8">
<title>Morvel — Business Card</title>
<link href="https://fonts.googleapis.com/css2?family=Alegreya+Sans+SC:wght@400&display=swap" rel="stylesheet">
<style>
  :root {
    --backdrop: #ececec;
    --card-dark: #3b3e40;
    --card-light: #ffffff;
    --panel: #e6e7e8;
    --brand-blue: #29a8df;
    --ink: #3c3f41;
    --shadow: 0 3px 6px rgba(0, 0, 0, 0.28);
  }
  * { margin: 0; padding: 0; box-sizing: border-box; }
  html, body {
    width: 878px;
    height: 1200px;
    overflow: hidden;
    background: var(--backdrop);
    font-family: "Alegreya Sans SC", "Helvetica Neue", Arial, sans-serif;
  }
  .sheet { position: relative; width: 878px; height: 1200px; }

  .card {
    position: absolute;
    width: 660px;
    height: 407px;
    box-shadow: var(--shadow);
  }

  /* Front: logo side */
  .card--front {
    left: 112px;
    top: 123px;
    background: var(--card-dark);
    display: flex;
    align-items: center;
    justify-content: center;
  }
  .brand-name {
    color: var(--brand-blue);
    font-size: 92px;
    font-weight: 400;
    letter-spacing: 2px;
    line-height: 1;
  }

  /* Back: contact side */
  .card--back {
    left: 115px;
    top: 651px;
    background: var(--card-light);
  }
  .card__panel {
    position: absolute;
    left: 34px;
    top: 33px;
    width: 590px;
    height: 343px;
    background: var(--panel);
  }
  .contact-name {
    position: absolute;
    left: 0;
    width: 100%;
    top: 158px;
    text-align: center;
    color: var(--brand-blue);
    font-size: 56px;
    font-weight: 400;
    letter-spacing: 2px;
    line-height: 1;
  }
  .contact-role {
    position: absolute;
    left: 0;
    width: 100%;
    top: 228px;
    text-align: center;
    color: var(--ink);
    font-size: 22px;
    letter-spacing: 4px;
    line-height: 1;
  }
  .contact-list {
    position: absolute;
    left: 46px;
    top: 292px;
    display: flex;
    gap: 18px;
    list-style: none;
    color: var(--ink);
    font-size: 15px;
    letter-spacing: 1.2px;
    line-height: 1;
    white-space: nowrap;
  }
  .contact-list__item { display: flex; align-items: center; gap: 8px; }
  .contact-list__icon { width: 16px; height: 16px; flex: none; }
</style>
</head>
<body>
<main class="sheet">
  <section class="card card--front" aria-label="Business card front">
    <span class="brand-name">morvel</span>
  </section>

  <section class="card card--back" aria-label="Business card back">
    <div class="card__panel"></div>
    <h1 class="contact-name">Peter Lang</h1>
    <p class="contact-role">Founder</p>
    <ul class="contact-list">
      <li class="contact-list__item">
        <svg class="contact-list__icon" viewBox="0 0 16 16" aria-hidden="true">
          <path d="M4 1.5 L6.2 4.8 L4.8 6.3 C5.8 8.4 7.6 10.2 9.7 11.2 L11.2 9.8 L14.5 12 L13 14.5 C7 14.3 1.7 9 1.5 3 Z" fill="#29a8df"/>
        </svg>
        <span>+381 64 70 81 925</span>
      </li>
      <li class="contact-list__item">
        <svg class="contact-list__icon" viewBox="0 0 16 16" aria-hidden="true">
          <rect x="1" y="3.5" width="14" height="9" fill="none" stroke="#29a8df" stroke-width="1.4"/>
          <path d="M1 3.5 L8 9 L15 3.5" fill="none" stroke="#29a8df" stroke-width="1.4"/>
        </svg>
        <span>peter.lang@morvel.com</span>
      </li>
      <li class="contact-list__item">
        <svg class="contact-list__icon" viewBox="0 0 16 16" aria-hidden="true">
          <circle cx="6.5" cy="6.5" r="4.6" fill="none" stroke="#29a8df" stroke-width="1.8"/>
          <path d="M10 10 L14.5 14.5" stroke="#29a8df" stroke-width="2.2" stroke-linecap="round"/>
        </svg>
        <span>www.morvel.com</span>
      </li>
    </ul>
  </section>
</main>
</body>
</html>
```